Job Posting for Licensed Veterinary Technician

We would like an eye catching job posting that we can send to technician schools in order to recruit veterinary technicians (LVTs) to our veterinary hospital

```html
<!DOCTYPE html>
<html lang="en">
<head>
<meta charset="utf-8">
<title>Harbor Point Veterinary Hospital – We're Hiring</title>
<link href="https://fonts.googleapis.com/css2?family=Montserrat:wght@400;500;700;800;900&display=swap" rel="stylesheet">
<style>
  :root {
    --bg: #2b2b2b;
    --paper: #ffffff;
    --lime: #9dc43f;
    --forest: #3f6b35;
    --teal: #1a8ca8;
    --teal-dark: #117892;
    --ink: #3a3a3a;
    --badge-red: #d0202a;
    --photo-light: #e9e4df;
    --photo-mid: #c7a585;
  }
  * { margin: 0; padding: 0; box-sizing: border-box; }
  html, body { width: 1200px; height: 2247px; overflow: hidden; background: var(--bg); }
  body { position: relative; font-family: 'Montserrat', sans-serif; color: var(--ink); }

  .flyer {
    position: absolute; left: 56px; top: 353px;
    width: 680px; height: 963px;
    background: var(--paper);
    transform: scale(1.6); transform-origin: top left;
    overflow: hidden;
    box-shadow: 0 6px 20px rgba(0,0,0,.5);
  }
  .hero-art { position: absolute; left: 0; top: 0; width: 680px; height: 380px; }

  .brand { position: absolute; left: 30px; top: 70px; width: 240px; display: flex; align-items: center; gap: 8px; }
  .brand-dot { width: 26px; height: 26px; border-radius: 50%; background: var(--teal); flex: none; }
  .brand-name { font-weight: 700; font-size: 17px; line-height: 1.2; color: var(--forest); }

  .headline { position: absolute; left: 30px; top: 182px; font-weight: 800; line-height: .92; }
  .headline .line1 { display: block; font-size: 66px; color: var(--lime); letter-spacing: 1px; }
  .headline .line2 { display: block; font-size: 66px; font-weight: 900; color: var(--forest); }

  .section-title { font-weight: 800; color: var(--teal); font-size: 21px; }
  .rule { display: block; width: 140px; height: 3px; margin-top: 8px; background: linear-gradient(90deg, var(--forest) 25%, transparent 25%, transparent 28%, var(--forest) 28%); }

  .job-desc { position: absolute; left: 33px; top: 328px; width: 312px; }
  .job-desc p { margin-top: 14px; font-size: 9.1px; line-height: 12.6px; }

  .job-type { position: absolute; left: 32px; top: 596px; width: 278px; height: 54px; border: 3px solid var(--forest); border-radius: 10px; display: flex; overflow: hidden; }
  .job-type .label { flex: 0 0 138px; display: flex; align-items: center; justify-content: center; font-weight: 800; font-size: 20px; color: #222; }
  .job-type .values { flex: 1; background: var(--forest); border-radius: 8px 0 0 8px; color: #fff; font-weight: 500; font-size: 16px; display: flex; flex-direction: column; justify-content: center; padding-left: 14px; line-height: 26px; }

  .offer { position: absolute; left: 32px; top: 668px; width: 320px; }
  .qualify { position: absolute; left: 360px; top: 742px; width: 300px; }

  .tick-list { list-style: none; margin-top: 14px; font-size: 10.5px; line-height: 13px; }
  .tick-list li { position: relative; padding-left: 18px; margin-bottom: 4px; }
  .tick-list li::before { content: "✓"; position: absolute; left: 0; top: 1px; width: 10px; height: 10px; border: 1.3px solid var(--forest); border-radius: 50%; font-size: 7px; line-height: 8px; text-align: center; color: var(--forest); font-weight: 700; }

  .duties { position: absolute; left: 360px; top: 376px; width: 300px; }
  .duties-title { font-size: 21px; line-height: 26px; color: var(--teal); font-weight: 500; }
  .duties-title strong { font-weight: 800; }
  .paw-list { list-style: none; margin-top: 16px; font-size: 10.5px; line-height: 12px; }
  .paw-list li { position: relative; padding-left: 20px; margin-bottom: 6px; }
  .paw-list li::before { content: ""; position: absolute; left: 1px; top: 2px; width: 8px; height: 8px; border-radius: 50%; background: var(--lime); box-shadow: -2px -3px 0 -2px var(--lime), 2px -3px 0 -2px var(--lime); }

  .badge { position: absolute; left: 32px; top: 887px; width: 58px; height: 58px; background: var(--badge-red); }

  .footer-band { position: absolute; left: 0; top: 920px; width: 680px; height: 43px; }
  .footer-note { position: absolute; left: 292px; top: 926px; font-size: 10px; line-height: 12.5px; color: #fff; }
</style>
</head>
<body>
  <main class="flyer">
    <svg class="hero-art" viewBox="0 0 680 380" aria-hidden="false">
      <defs>
        <linearGradient id="photoTone" x1="0" y1="0" x2="1" y2="1">
          <stop offset="0" stop-color="var(--photo-light)"/>
          <stop offset=".55" stop-color="var(--photo-mid)"/>
          <stop offset="1" stop-color="#f2f2f2"/>
        </linearGradient>
      </defs>
      <circle cx="515" cy="135" r="230" fill="var(--teal)"/>
      <circle cx="540" cy="115" r="215" fill="var(--paper)"/>
      <circle cx="548" cy="105" r="205" fill="url(#photoTone)" role="img" aria-label="Photo of a smiling veterinary technician in a white coat holding a small terrier dog"/>
    </svg>

    <div class="brand">
      <span class="brand-dot"></span>
      <span class="brand-name">Harbor Point Veterinary Hospital</span>
    </div>

    <h1 class="headline"><span class="line1">WE’RE</span><span class="line2">HIRING</span></h1>

    <section class="job-desc">
      <h2 class="section-title">JOB DESCRIPTION</h2>
      <span class="rule"></span>
      <p>Harbor Point Veterinary Hospital (412 Elm Avenue in Riverton) is growing and excited to announce an opening for a part- or full-time Licensed Veterinary Technician. Our new Hospital opened in late 2015 and is a full service medical, dental and surgical center with a focus on preventive medicine. We are also equipped and able to handle most daytime emergency cases.<br>Applicants must be energetic, compassionate, welcoming, positive, and enjoy interfacing with both clients and pets. An extraordinary attention to detail in caring for our clients' and patients' needs is a must. We are a paperless facility, and expertise in electronic medical records or the ability to quickly learn these systems is required.<br>Harbor Point Veterinary Hospital is NVHA-Accredited, and our medical staff are all Calm Care Certified. We are located in the historic Harbor Point neighborhood of Riverton, minutes from Downtown Riverton and the beaches of Riverton and Sandy Cove.</p>
    </section>

    <div class="job-type">
      <div class="label">JOB TYPE</div>
      <div class="values"><span>FULL TIME</span><span>PART TIME</span></div>
    </div>

    <section class="offer">
      <h2 class="section-title">We Offer:</h2>
      <span class="rule"></span>
      <ul class="tick-list">
        <li>Very competitive compensation based on<br>skills and experience</li>
        <li>Employer-sponsored retirement plan with<br>matching contributions</li>
        <li>Short and long term disability insurance (100%<br>employer paid for FT)</li>
        <li>Medical insurance (employer contributions for FT)</li>
        <li>Life insurance (100% employer paid for FT)</li>
        <li>Employee discounts</li>
        <li>Vacation time and holiday pay for full time employees</li>
      </ul>
    </section>

    <section class="duties">
      <h2 class="duties-title">You Duties <strong>May Include,</strong><br>But Are <strong>Not Limited To</strong></h2>
      <span class="rule"></span>
      <ul class="paw-list">
        <li>Ensure the best possible client/patient<br>experience.</li>
        <li>Take digital radiographs.</li>
        <li>Venapuncture.</li>
        <li>IV catheter placement</li>
        <li>Blood pressure monitoring.</li>
        <li>Induction and monitoring of anesthesia.</li>
        <li>Administration and logging of controlled<br>medications</li>
        <li>Run/Process lab work.</li>
        <li>Assist and monitor in surgery.</li>
        <li>Educate clients.</li>
        <li>Discharge patients.</li>
        <li>Share ideas.</li>
        <li>Discuss cases.</li>
        <li>Medicate and restrain patients.</li>
      </ul>
    </section>

    <section class="qualify">
      <h2 class="section-title">Qualifications:</h2>
      <span class="rule"></span>
      <ul class="tick-list">
        <li>LVT, licensed to practice in the Commonwealth<br>of Virginia.</li>
        <li>Excellent people skills.</li>
        <li>Team player.</li>
        <li>Proficient in technical skills and excited to use them.</li>
        <li>Ability to complete above duties</li>
      </ul>
    </section>

    <div class="badge" role="img" aria-label="Accreditation badge"></div>

    <svg class="footer-band" viewBox="0 0 680 43" aria-hidden="true">
      <polygon points="278,0 680,0 680,43 250,43" fill="var(--forest)"/>
    </svg>
    <p class="footer-note">* Only applicants who apply through this posting will be considered.<br>NO in-person applicants will be considered *</p>
  </main>
</body>
</html>
```